Hair dresser flyer for Air conditioning heat pumps A5

We require a flyer that is selling the benifits of air conditioning heat pumps which cools in summer and efficently heats in winter. Colour should be white background. Red and blue from logo to represent the Air conditioning Heat pump does heating and cooling and energy effient.

Target Market(s)

Hairdressor, Salons , barbers ,

Colors
0054AA
0677BA
7BADD7
CADEEF
E8F1F8
EB3D1F
EC4F4E
F09395
F8D3D4
FCEDEE

Requirements
Must have
• Cost from

```html
<!DOCTYPE html>
<html lang="en">
<head>
<meta charset="utf-8">
<title>Harlow – Air Conditioning Heat Pump Flyer</title>
<link rel="stylesheet" href="https://fonts.googleapis.com/css2?family=Archivo+Black&family=Arimo:wght@400;700&display=swap">
<style>
  :root{
    --blue:#2fa6de;
    --blue-deep:#0677BA;
    --blue-pale:#CADEEF;
    --red:#EB4F1F;
    --red-deep:#EB3D1F;
    --ink:#111;
    --paper:#fff;
    --stage:#000;
    --display:"Archivo Black", sans-serif;
    --body:"Arimo", sans-serif;
  }
  *{box-sizing:border-box;margin:0;padding:0}
  html,body{width:1200px;height:930px;overflow:hidden;background:var(--stage)}
  .stage{position:relative;width:1200px;height:930px}
  .page{position:absolute;top:95px;width:497px;height:696px;background:var(--paper);overflow:hidden;font-family:var(--body);color:var(--ink)}
  .page--front{left:87px}
  .page--back{left:618px}

  /* brand */
  .brand{position:absolute;left:22px;top:40px;display:flex;align-items:center;gap:10px}
  .brand__mark{width:12px;height:12px;background:var(--red)}
  .brand__name{font-family:var(--body);font-weight:700;font-size:38px;line-height:40px;color:var(--ink)}

  /* photo placeholders */
  .photo{position:absolute}
  .photo--salon{left:254px;top:0;width:243px;height:212px;
    clip-path:polygon(0 0,100% 0,100% 100%,48px 100%,48px 101px,0 101px);
    background:linear-gradient(160deg,#5d5f63 0%,#8d8b88 35%,#d9d6d2 65%,#b9b4ae 100%)}
  .photo--unit{left:272px;top:378px;width:204px;height:228px;
    background:radial-gradient(ellipse at 45% 45%,#f3f3f3 0%,#e2e2e2 55%,#fff 100%)}
  .photo--cassette{left:234px;top:0;width:263px;height:130px;
    background:linear-gradient(180deg,#f4f2f4 0%,#ece7ec 55%,#d6a9bc 80%,#a47a8f 100%)}
  .photo--room{left:29px;top:275px;width:214px;height:150px;
    background:linear-gradient(135deg,#f6e5e4 0%,#efd0cd 50%,#c7b3a6 100%)}
  .photo--wallunit{left:244px;top:256px;width:253px;height:172px;
    background:linear-gradient(90deg,#f2f7fb 0%,#e3eef7 45%,#1f1f1f 46%,#2b2b2b 85%,var(--blue) 86%)}
  .photo--team{left:0;top:430px;width:497px;height:175px;
    background:linear-gradient(180deg,#9fb3c4 0%,#c6ccd1 30%,#8a8c8e 60%,#5d5f61 100%)}

  /* front */
  .save{position:absolute;top:108px;left:0;height:67px;display:flex}
  .save__word{font-family:var(--display);color:#fff;font-size:49px;line-height:67px;text-align:center}
  .save__word--blue{background:var(--blue);width:173px}
  .save__word--red{background:var(--red);width:123px}
  .subhead{position:absolute;left:20px;top:176px;font-family:var(--display);font-weight:400;color:var(--red);font-size:16.5px;line-height:21px;letter-spacing:.2px}
  .intro{position:absolute;left:20px;top:232px;width:266px;font-size:7.6px;line-height:9.7px;text-align:justify}
  .intro p{margin-bottom:9px}
  .offer{position:absolute;left:302px;top:220px;width:195px;height:62px;background:var(--blue);color:#fff;padding:7px 0 0 15px}
  .offer__title{font-family:var(--display);font-size:16.5px;line-height:19px}
  .offer__text{font-family:var(--body);font-weight:700;font-size:10.5px;line-height:13px}
  .price{position:absolute;left:302px;top:282px;width:195px;height:73px;background:var(--red);color:#fff;
    clip-path:polygon(0 0,100% 0,100% 100%,70% 100%,66% 86%,0 86%)}
  .price__amount{position:absolute;left:12px;top:2px;font-family:var(--display);font-size:48px;line-height:56px;letter-spacing:-.5px}
  .price__vat{position:absolute;right:25px;top:53px;font-weight:700;font-size:10.5px}
  .benefits{position:absolute;left:38px;top:361px;list-style:none}
  .benefits li{height:28.4px;display:flex;align-items:center;gap:11px;font-size:10.4px;letter-spacing:1.5px}
  .benefits svg{width:26px;height:26px;flex:none}
  .benefits text{font-family:var(--body);font-weight:700;font-size:8px;fill:#fff}
  .call{position:absolute;left:276px;top:607px;font-family:var(--display);font-size:16px;color:var(--red)}

  /* back */
  .headline{position:absolute;left:0;top:112px;width:277px;height:72px;background:var(--blue);color:#fff;
    font-family:var(--display);font-weight:400;font-size:16.5px;line-height:20.5px;padding:4px 0 0 28px;
    clip-path:polygon(0 0,96% 0,100% 25%,100% 100%,0 100%)}
  .example{position:absolute;left:277px;top:130px;width:189px;height:122px;background:var(--red);color:#fff;
    font-family:var(--body);font-weight:700;font-size:8.2px;line-height:9.8px;padding:15px 8px 0 12px}
  .example p{margin-bottom:9px}
  .example-fade{position:absolute;left:466px;top:140px;width:31px;height:100px;background:linear-gradient(90deg,var(--blue-pale),#fff)}
  .explain{position:absolute;left:29px;top:196px;width:216px;font-size:7.7px;line-height:9.7px;text-align:justify}
  .explain p{margin-bottom:9px}
  .app-callout{position:absolute;left:306px;top:557px;width:191px;height:48px;background:var(--blue);color:#fff;
    clip-path:polygon(10% 0,84% 0,100% 100%,0 100%);font-size:9.4px;line-height:11.5px;text-align:center;padding:4px 30px 0 14px}
  .closing{position:absolute;left:0;top:613px;width:497px;text-align:center;font-size:9.2px}

  /* footer */
  .footer{position:absolute;left:0;top:634px;width:497px;height:62px;display:flex;color:#fff;font-family:var(--display)}
  .footer__web,.footer__phone{display:flex;align-items:center;gap:10px;font-size:17.5px;letter-spacing:.5px}
  .footer__web{background:var(--blue);width:248px;padding-left:29px}
  .footer__phone{background:var(--red);flex:1;padding-left:26px}
  .footer svg{width:24px;height:24px;flex:none}
</style>
</head>
<body>
<svg width="0" height="0" style="position:absolute">
  <defs>
    <symbol id="flake" viewBox="0 0 26 26">
      <g stroke="#2fa6de" stroke-width="1.6" stroke-linecap="round" fill="none">
        <path d="M13 1v24M1 13h24M4.5 4.5l17 17M21.5 4.5l-17 17"/>
        <path d="M10 2.5l3 3 3-3M10 23.5l3-3 3 3M2.5 10l3 3-3 3M23.5 10l-3 3 3 3"/>
      </g>
      <circle cx="13" cy="13" r="6" fill="#EB4F1F" stroke="#fff" stroke-width="1"/>
    </symbol>
    <symbol id="globe" viewBox="0 0 24 24">
      <g fill="none" stroke="#fff" stroke-width="1.5">
        <circle cx="12" cy="12" r="10.5"/><ellipse cx="12" cy="12" rx="4.5" ry="10.5"/>
        <path d="M1.5 12h21M3.5 6.5h17M3.5 17.5h17"/>
      </g>
    </symbol>
    <symbol id="phone" viewBox="0 0 24 24">
      <circle cx="12" cy="12" r="11" fill="#fff"/>
      <path d="M8.2 5.5l2.2 3-1.3 1.6c.7 1.9 2 3.3 3.9 4.2l1.6-1.3 3 2.2-1.3 2.6c-4.9-.4-9.1-4.6-9.5-9.5z" fill="#EB4F1F"/>
    </symbol>
  </defs>
</svg>

<main class="stage">
  <!-- Front page -->
  <section class="page page--front">
    <div class="brand"><span class="brand__mark"></span><span class="brand__name">Harlow</span></div>
    <div class="photo photo--salon" role="img" aria-label="Hair salon interior with a ceiling cassette air conditioning unit"></div>

    <div class="save"><div class="save__word save__word--blue">SAVE</div><div class="save__word save__word--red">£££</div></div>
    <h2 class="subhead">on your Shops Heating costs<br>And stay Cool in the Summer</h2>

    <div class="intro">
      <p>Air Conditioning Heat Pumps creates the ideal environment all year round for staff to be at there most productive and for consumers to spend more time and, accordingly, more money.</p>
      <p>Modern Air Conditioning Heat pumps are one of the most energy efficient forms of heating available and ideal for those looking for a simple cost effective way to heat and cool the space. They are easy to install &amp; operate and can quickly provide with the comfort you need.</p>
      <p>Reduce cancelations and absences in the warm summer months with Cooling mode. With the warms temperatures inside hairdressers and salons and clients not wanting to sit in somewhere with extreme heat,</p>
    </div>

    <div class="offer">
      <div class="offer__title">Energy- Efficient</div>
      <div class="offer__text">Air Conditioning Heat Pumps<br>installed from</div>
    </div>
    <div class="price"><span class="price__amount">£1750</span><span class="price__vat">+ Vat</span></div>

    <ul class="benefits">
      <li><svg viewBox="0 0 26 26"><use href="#flake"/><text x="13" y="16" text-anchor="middle">1</text></svg>COOLS IN SUMMER</li>
      <li><svg viewBox="0 0 26 26"><use href="#flake"/><text x="13" y="16" text-anchor="middle">2</text></svg>EFFICIENT HEATS IN WINTER</li>
      <li><svg viewBox="0 0 26 26"><use href="#flake"/><text x="13" y="16" text-anchor="middle">3</text></svg>MORE PRODUCTIVE STAFF</li>
      <li><svg viewBox="0 0 26 26"><use href="#flake"/><text x="13" y="16" text-anchor="middle">4</text></svg>INCREASED SALES</li>
      <li><svg viewBox="0 0 26 26"><use href="#flake"/><text x="13" y="16" text-anchor="middle">5</text></svg>REDUCE CANCELLATION IN</li>
      <li><svg viewBox="0 0 26 26"><use href="#flake"/><text x="13" y="16" text-anchor="middle">6</text></svg>SUMMER</li>
      <li><svg viewBox="0 0 26 26"><use href="#flake"/><text x="13" y="16" text-anchor="middle">7</text></svg>FILTERS AND CLEANS THE AIR</li>
      <li><svg viewBox="0 0 26 26"><use href="#flake"/><text x="13" y="16" text-anchor="middle">8</text></svg>REDUCED ALLERGENS &amp; BUGS</li>
      <li><svg viewBox="0 0 26 26"><use href="#flake"/><text x="13" y="16" text-anchor="middle">9</text></svg>REDUCE HUMIDITY</li>
    </ul>

    <div class="photo photo--unit" role="img" aria-label="Outdoor air source heat pump unit with warm air flow arrows"></div>
    <div class="call">Call on</div>

    <footer class="footer">
      <div class="footer__web"><svg><use href="#globe"/></svg>www.harlow.cool</div>
      <div class="footer__phone"><svg><use href="#phone"/></svg>01632 960418</div>
    </footer>
  </section>

  <!-- Back page -->
  <section class="page page--back">
    <div class="photo photo--cassette" role="img" aria-label="Ceiling cassette air conditioner above a flower wall"></div>
    <div class="brand"><span class="brand__mark"></span><span class="brand__name">Harlow</span></div>

    <h2 class="headline">Reduce heating energy<br>cost by up to 75% vs<br>electric heating.</h2>
    <div class="example-fade"></div>
    <div class="example">
      <p>Here's an example to illustrate how<br>an air-to-air heat pump can save you<br>money over an electric&nbsp; heaters</p>
      <p>2 x 2kw Electric fan heaters 4kw<br>Electricity input&nbsp; =&nbsp;&nbsp; 4kw heat Output</p>
      <p>4kw Air Conditioning heat pump 1kw<br>Electricty input =&nbsp; 4kw Heat output</p>
    </div>

    <div class="explain">
      <p>Air conditioning heat pumps is a more efficient heating solution in comparison to a standard electric heaters which are still used in many businesses.</p>
      <p>This is because air conditioning produces more heat for the amount of electricity it takes to power the unit.</p>
    </div>

    <div class="photo photo--wallunit" role="img" aria-label="Black wall-mounted air conditioning unit on a blue band"></div>
    <div class="photo photo--room" role="img" aria-label="Pink salon room with a white wall-mounted air conditioner"></div>
    <div class="photo photo--team" role="img" aria-label="Installation team standing beside branded vans on a seafront, with a hand holding a phone app"></div>
    <div class="app-callout">Control Your<br>Air Source Heat Pump<br>right from your Phone</div>

    <p class="closing">If you are interested in having air conditioning installed in your business, then give us a call on</p>

    <footer class="footer">
      <div class="footer__web"><svg><use href="#globe"/></svg>www.harlow.cool</div>
      <div class="footer__phone"><svg><use href="#phone"/></svg>01632 960418</div>
    </footer>
  </section>
</main>
</body>
</html>
```